Warren D Pellham New Business Card Design

I assist families or individuals with downsizing. When they need to sell estate items I manage the process. I may buy their items. I may place their items with auction houses or I may bring in a variety of experts to sell all of the items. We help clients sell a huge variety of items including art, jewelry, coins, watches, antiques, collectibles, etc.

Target Market(s)

Two markets...One market is the clients I serve which are usually seniors or their family. These are individuals that need to sell on item or a house full if they estate is being liquidated. The other market is those that refer clients to me. Real Estate professionals, active senior communities, trust and estate lawyers and financial advisors.

Contact Information for Business Card

This is a new business so we do not have a logo. We may not need a logo. Feel free to visit our website at www.warrendpellham-example.com for more information on the service we provide. I am a private consultant so my name needs to be prominent. My name is my brand. We need the card to let people know how to contact us via phone, website and email. Easy to read. Many of our clients are elderly.

Font styles to use
Sans Serif

Requirements
Must have
• My name. Our contact information.
• Warren D Pellham
• 555-218-7034 Office
• 555-639-1582 Cell
• info@warrendpellham-example.com
• www.warrendpellham-example.com

```html
<!DOCTYPE html>
<html lang="en">
<head>
<meta charset="utf-8">
<title>Warren D Pellham — Business Card</title>
<link href="https://fonts.googleapis.com/css2?family=Bebas+Neue&family=Montserrat:wght@400;500&display=swap" rel="stylesheet">
<style>
  :root {
    --page: #e9e6e2;
    --card: #3b342d;
    --accent: #cbb497;
    --accent-light: #e6d6c0;
    --ink: #f4f1ec;
    --muted: #b9ab98;
    --photo-a: #d9d2c6;
    --photo-b: #4a4b58;
  }
  * { margin: 0; padding: 0; box-sizing: border-box; }
  html, body { width: 1200px; height: 900px; overflow: hidden; }
  body {
    background: var(--page);
    position: relative;
    font-family: "Montserrat", sans-serif;
  }
  .card {
    position: absolute;
    left: 250px;
    width: 700px;
    height: 400px;
    border-radius: 22px;
    background: var(--card);
    box-shadow: 0 10px 28px rgba(0,0,0,0.22);
    overflow: hidden;
  }
  .card-front { top: 40px; }
  .card-back { top: 460px; }

  .front-name {
    position: absolute;
    inset: 0;
    display: flex;
    align-items: center;
    justify-content: center;
    font-family: "Bebas Neue", sans-serif;
    font-weight: 400;
    font-size: 74px;
    letter-spacing: 1px;
    color: var(--accent);
  }

  .portrait {
    position: absolute;
    right: 42px;
    top: 46px;
    width: 240px;
    height: 210px;
    background: linear-gradient(160deg, var(--photo-a) 0%, #b7aea3 45%, var(--photo-b) 100%);
  }

  .identity {
    position: absolute;
    left: 58px;
    top: 158px;
    display: flex;
    align-items: stretch;
    gap: 16px;
  }
  .identity-bar {
    width: 12px;
    background: var(--accent-light);
  }
  .identity-name {
    font-family: "Bebas Neue", sans-serif;
    font-weight: 400;
    font-size: 48px;
    line-height: 0.95;
    color: var(--accent);
    letter-spacing: 0.5px;
  }
  .identity-role {
    font-family: "Bebas Neue", sans-serif;
    font-size: 14px;
    letter-spacing: 0.6px;
    color: var(--accent);
    margin-top: 2px;
  }

  .contact-list {
    position: absolute;
    left: 110px;
    top: 240px;
    list-style: none;
  }
  .contact-item {
    display: flex;
    align-items: center;
    gap: 14px;
    font-size: 18px;
    color: var(--ink);
    height: 31px;
    white-space: nowrap;
  }
  .contact-icon { width: 20px; height: 20px; flex: none; }
  .contact-label {
    font-size: 13px;
    color: var(--muted);
    text-transform: uppercase;
    letter-spacing: 1px;
  }
  .contact-item .highlight { color: var(--accent); }
</style>
</head>
<body>

  <section class="card card-front" aria-label="Card front">
    <h1 class="front-name">Warren D Pellham</h1>
  </section>

  <section class="card card-back" aria-label="Card back">
    <div class="portrait" role="img" aria-label="Portrait photo of Warren D Pellham"></div>

    <div class="identity">
      <span class="identity-bar"></span>
      <div>
        <h2 class="identity-name">Warren D Pellham</h2>
        <p class="identity-role">Collectable Asset Buyer, Broker &amp; Consultant</p>
      </div>
    </div>

    <ul class="contact-list">
      <li class="contact-item">
        <svg class="contact-icon" viewBox="0 0 24 24" aria-hidden="true">
          <path fill="#f4f1ec" d="M3 9c0-3 4-5 9-5s9 2 9 5v2h-5V9c-1-.6-2.4-1-4-1s-3 .4-4 1v2H3z"/>
          <rect x="5" y="12" width="14" height="8" rx="2" fill="#f4f1ec"/>
          <circle cx="12" cy="16" r="2" fill="#3b342d"/>
        </svg>
        <span>555-218-7034</span>
        <span class="contact-label">Office</span>
      </li>
      <li class="contact-item">
        <svg class="contact-icon" viewBox="0 0 24 24" aria-hidden="true">
          <rect x="6" y="2" width="12" height="20" rx="2.5" fill="#f4f1ec"/>
          <rect x="8" y="5" width="8" height="12" fill="#3b342d"/>
          <circle cx="12" cy="19.3" r="1.1" fill="#3b342d"/>
        </svg>
        <span>555-639-1582</span>
        <span class="contact-label">Cell</span>
      </li>
      <li class="contact-item">
        <svg class="contact-icon" viewBox="0 0 24 24" aria-hidden="true">
          <path fill="#f4f1ec" d="M21 3 3 11l7 2 2 8z"/>
        </svg>
        <span>info@warrendpellham-example.com</span>
      </li>
      <li class="contact-item">
        <svg class="contact-icon" viewBox="0 0 24 24" aria-hidden="true">
          <circle cx="12" cy="12" r="9" fill="none" stroke="#f4f1ec" stroke-width="2"/>
          <ellipse cx="12" cy="12" rx="4" ry="9" fill="none" stroke="#f4f1ec" stroke-width="1.6"/>
          <line x1="3" y1="12" x2="21" y2="12" stroke="#f4f1ec" stroke-width="1.6"/>
        </svg>
        <span>www.<span class="highlight">warrendpellham-example</span>.com</span>
      </li>
    </ul>
  </section>

</body>
</html>
```